Business Card Design Project

Hi!
Looking for a business card design for my acupuncture/remedial massage business using a logo I've just had designed through this site!
I'd like the following details included:
Logo (obviously)
My name - Miranda Pellowtane
Clinic details -Complementary and Traditional Chinese Medicine Haven
42 Brindlewood Road
Ashcombe Vale 3162
03 9471 6820
Website - www.pellowtanewell.com.au
I have the logo design in two different colour combinations, one predominantly green, and the other in reverse colours. I was thinking that the green logo would take up one whole side of the business card, then we could include the reverse logo on the more detailed side. I'd like to see how that looks.
I also had the idea that the heart in the logo could be printed in metallic red (depending on cost). Not sure if that comes into play now or at the printers.
Thanks!

```html
<!DOCTYPE html>
<html lang="en">
<head>
<meta charset="utf-8">
<title>Pellowtane Well – Business Card</title>
<link href="https://fonts.googleapis.com/css2?family=Noto+Sans:wght@400;600&display=swap" rel="stylesheet">
<style>
  :root {
    --canvas: #000000;
    --green: #00b386;
    --green-soft: #4fc19a;
    --mist: #f1f7f4;
    --white: #ffffff;
    --red: #e3262b;
    --text-font: "Noto Sans", Arial, sans-serif;
  }
  * { box-sizing: border-box; margin: 0; padding: 0; }
  html, body { width: 1000px; height: 1200px; overflow: hidden; background: var(--canvas); }
  body { position: relative; font-family: var(--text-font); }

  .card { position: absolute; overflow: hidden; }
  .card-shapes { position: absolute; inset: 0; width: 100%; height: 100%; }

  /* Front */
  .card--front { left: 120px; top: 95px; width: 733px; height: 451px; background: var(--green); }
  .front-mark {
    position: absolute; left: 0; right: 0; top: 110px;
    text-align: center; color: var(--white);
    font-weight: 600; font-size: 66px; line-height: 1.1; letter-spacing: -0.5px;
  }
  .front-website {
    position: absolute; left: 0; right: 0; top: 374px;
    text-align: center; color: var(--green); font-size: 27px; font-weight: 400;
  }

  /* Back */
  .card--back { left: 117px; top: 653px; width: 728px; height: 448px; background: var(--white); }
  .back-mark {
    position: absolute; left: 60px; top: 150px; width: 260px;
    text-align: center; color: var(--green);
    font-weight: 600; font-size: 46px; line-height: 1.15; letter-spacing: -0.5px;
  }
  .divider { position: absolute; left: 364px; top: 65px; width: 2px; height: 280px; background: var(--green); }
  .contact { position: absolute; right: 60px; top: 90px; text-align: right; }
  .contact-name { color: var(--red); font-size: 26px; font-weight: 400; line-height: 36px; margin-bottom: 26px; }
  .contact-clinic { color: var(--green); font-size: 16px; line-height: 27px; margin-bottom: 23px; }
  .contact-line { color: var(--red); font-size: 16px; line-height: 27px; display: flex; justify-content: flex-end; align-items: center; gap: 6px; }
  .contact-address { margin-bottom: 19px; }
  .contact-icon { width: 22px; height: 22px; flex: none; }
</style>
</head>
<body>

<section class="card card--front">
  <svg class="card-shapes" viewBox="0 0 733 451" aria-hidden="true">
    <circle cx="355" cy="195" r="240" fill="none" stroke="var(--green-soft)" stroke-width="18"/>
    <path d="M0 405 Q 330 300 733 415 L733 451 L0 451 Z" fill="var(--white)"/>
  </svg>
  <div class="front-mark">Pellowtane<br>Well</div>
  <p class="front-website">www.pellowtanewell.com.au</p>
</section>

<section class="card card--back">
  <svg class="card-shapes" viewBox="0 0 728 448" aria-hidden="true">
    <rect x="0" y="0" width="728" height="23" fill="var(--green)"/>
    <circle cx="540" cy="225" r="215" fill="none" stroke="var(--mist)" stroke-width="18"/>
    <path d="M0 424 Q 370 330 728 426 L728 448 L0 448 Z" fill="var(--green)"/>
  </svg>
  <div class="back-mark">Pellowtane<br>Well</div>
  <div class="divider"></div>
  <div class="contact">
    <p class="contact-name">Miranda Pellowtane</p>
    <p class="contact-clinic">Complementary and Traditional<br>Chinese Medicine Haven</p>
    <div class="contact-address">
      <p class="contact-line">
        <svg class="contact-icon" viewBox="0 0 22 22" aria-hidden="true">
          <circle cx="11" cy="11" r="10" fill="none" stroke="var(--red)" stroke-width="1.5"/>
          <path d="M11 17 C8 13 7.5 11.5 7.5 9.8 A3.5 3.5 0 0 1 14.5 9.8 C14.5 11.5 14 13 11 17 Z" fill="var(--red)"/>
          <circle cx="11" cy="9.8" r="1.3" fill="var(--white)"/>
        </svg>
        42 Brindlewood Road
      </p>
      <p class="contact-line">Ashcombe Vale 3162</p>
    </div>
    <p class="contact-line">
      <svg class="contact-icon" viewBox="0 0 22 22" aria-hidden="true">
        <circle cx="11" cy="11" r="10" fill="none" stroke="var(--red)" stroke-width="1.5"/>
        <path d="M7.5 6.5 L9.3 6.2 L10.3 8.8 L9.1 9.8 C9.8 11.3 10.8 12.3 12.2 13 L13.2 11.8 L15.8 12.8 L15.5 14.6 C15.3 15.3 14.6 15.7 13.8 15.6 C10.2 15 7 11.8 6.4 8.2 C6.3 7.4 6.8 6.7 7.5 6.5 Z" fill="var(--red)"/>
      </svg>
      03 9471 6820
    </p>
  </div>
</section>

</body>
</html>
```